Revamp business card for upcoming new practice

We need a business card with our new practice location details. We are a boutique dental practice. Our new practice design is timeless black, white and grey colour scheme with a pop of our purple.
We are moving away from the amount of purple on website and overall practice.
Simple, elegant, clean and eye catching.

Industry/Entity Type

Dental Clinic

Contact Information for Business Card

See Design brief attached

Font styles to use
Serif
Sans Serif

Requirements
Must have
• New design | Front requirements:
• • Business logo (see attached files)
• • Address: 214 Corwell Road Brinsley Vic 3172
• • Phone number: 03 9476 3815
• • Email: info@torvendental.example.au
• • Website address: torvendental.example.au
• New design | Back requirements:
• • Dentist Details: Dr. Leon Grubbe & Associates
• B.D.S Ashdown Hall Bristol
• Grad. Dip. Clin. Dent. (Conscious Sedation & Pain Control). University of Corrimal.
• • Your Next Appointment is: OR no text and just lines for writing an appointment
• • Lines for writing the appointment minimum 2, maximum 3.
• • Cancellation Policy: We require a minimum of 48 hours or a fee will apply
Nice to have
• Black, grey and white colours with the touch of purple
Should not have
• Icon/images for contact details
• Be entirely purple.

```html
<!DOCTYPE html>
<html lang="en">
<head>
<meta charset="utf-8">
<title>Torven Dental – Business Card</title>
<link rel="stylesheet" href="https://fonts.googleapis.com/css2?family=Open+Sans:wght@400;600&display=swap">
<style>
  :root {
    --purple: #8c4b9c;
    --charcoal: #3d3d3d;
    --paper: #ffffff;
    --text-light: #ffffff;
  }
  html, body {
    margin: 0;
    padding: 0;
    overflow: hidden;
    background: var(--paper);
  }
  .card {
    position: relative;
    width: 1200px;
    height: 685px;
    background: var(--paper);
    overflow: hidden;
    font-family: "Open Sans", Arial, sans-serif;
  }
  .brand-name {
    position: absolute;
    left: 100px;
    top: 92px;
    margin: 0;
    font-size: 150px;
    font-weight: 600;
    line-height: 1;
    letter-spacing: -2px;
    color: var(--purple);
    white-space: nowrap;
  }
  .info-band {
    position: absolute;
    left: 0;
    top: 358px;
    width: 1200px;
    height: 250px;
  }
  .contact {
    position: absolute;
    left: 58px;
    top: 382px;
    margin: 0;
    color: var(--text-light);
    font-size: 32px;
    line-height: 1;
  }
  .contact-address {
    margin: 0 0 18px;
    font-size: 32px;
    white-space: nowrap;
  }
  .contact-list {
    display: grid;
    grid-template-columns: 147px auto;
    row-gap: 13px;
    margin: 0;
  }
  .contact-label {
    color: var(--purple);
    margin: 0;
  }
  .contact-value {
    margin: 0;
    white-space: nowrap;
  }
</style>
</head>
<body>
  <main class="card">
    <h1 class="brand-name">TORVEN dental</h1>

    <svg class="info-band" viewBox="0 0 1200 250" aria-hidden="true">
      <polygon points="0,0 810,0 995,238 0,238" fill="var(--charcoal)"/>
      <rect x="0" y="238" width="1200" height="12" fill="var(--purple)"/>
    </svg>

    <address class="contact">
      <p class="contact-address">214 Corwell Road, Brinsley Vic 3172</p>
      <dl class="contact-list">
        <dt class="contact-label">phone</dt>
        <dd class="contact-value">03 9476 3815</dd>
        <dt class="contact-label">e-mail</dt>
        <dd class="contact-value">info@torvendental.example.au</dd>
        <dt class="contact-label">website</dt>
        <dd class="contact-value">torvendental.example.au</dd>
      </dl>
    </address>
  </main>
</body>
</html>
```